Funky Modern Flyer A5 or Postcard size

Hi, I am looking at a one small flyer (A5 or postcard size) that I can put both on my website on the front page (ie so png) and also send out if necessary.

It has to be modern, funky and hip. My brand is professional / Corporate so it also has to fit in with that brand.

There are 6 attachments:
Example 1 - Kavorra - I like this look, clean, modern, funky and says it all.
Example 2 - Kavora - again another look I like, simple, explanatory
Example 4 - Artisan Bazaar - font is cool on this one but background not so much too much going on but I like the font
Example 5 - Example 4 - Artisan Bazaar - font is cool on this one but background not so much too much going on but I like the font
5 is my logo
Example 6 is something I found on the web this morning which is effective.

It is for a Mentoring and Training program I run called: SKYWARD

What is to be included is the following:
The name: Skyward
Somewhere: Training, Mentoring
My Logo (see attached two options) you can choose which colour suits and I have the source file should you need it
My website and email: www.deliamarsk.example / delia@deliamarsk.example

This wording: This is one of our highest in-demand programs and is based on a background and proven track record by Delia in accelerating sales organisations and their people into stand out high performers. **(NOTE this wording in this paragraph may change and I am open to you changing if you think you can make it more effective!)

Colours: white, black and gold (those are our website colours).

I'd like the Skyward to really stand out.... I have included two fonts that I really like that I got off Artisan Bazaar. However, feel free to suggest other fonts that you think cool or funky!
Updates

Hi everyone, just to add a note to the brief, I am not overly keen on pictures that are really busy. I only like a picture that is minimal and effective. The examples from Artisan Bazaar was more for the Font Style not so much the pictures in the background. The pictures can take away from a design unless done really minimally.....hope this makes sense. Delia Added Wednesday, March 15, 2017

Target Market(s)

My target Market is Corporates but I want a Funky Modern look as a lot of people in Corporates are Millennials as well which is part of my target market

Industry/Entity Type

Information Technology

Requirements
Must have
• What is to be included is the following:
• The name: Skyward
• Somewhere: Training, Mentoring
• My Logo (see attached two options) you can choose which colour suits and I have the source file should you need it
• My website and email: www.deliamarsk.example / delia@deliamarsk.example
• This wording: This is one of our highest in-demand programs and is based on a background and proven track record in high performance and accelerating sales organisations and their people into stand out high performers. (**NOTE this wording may change when final design is picked to be changed as still working in it***)
• Colours: white, black and gold (those are our website colours).
• I'd like the Skyward to really stand out.... I have included two fonts that I really like that I got off Artisan Bazaar. However, feel free to suggest other fonts that you think cool or funky! NOTE: The pictures I have attached is mainly for the FONTS not for the background pictures. I am not that keen on background pictures as it can take away from the font - unless it is minimal
Should not have
• Too many different colours, I like slick, modern, clean. White, gold and black preferred as this is our website colour.
• NOTE: The pictures from Artisan Bazaar I have attached are mainly for the FONTS not for the background pictures. I am not hugely keen on background pictures as it can take away from the font/message - unless the pictures are minimal but effective.

```html
<!DOCTYPE html>
<html lang="en">
<head>
<meta charset="UTF-8">
<title>Skyward – Training &amp; Mentoring Flyer</title>
<link rel="stylesheet" href="https://fonts.googleapis.com/css2?family=Abril+Fatface&family=PT+Sans:wght@400;700&family=Raleway:wght@300&family=Oswald:wght@700&display=swap">
<style>
  :root {
    --black: #000000;
    --white: #ffffff;
    --gold: #d9b650;
    --gold-light: #f3dc8a;
    --gold-deep: #b8902f;
    --sky-top: #2b3f55;
    --sky-mid: #6c7a82;
    --horizon: #f0a21c;
    --water: #3a2a10;
  }
  html, body {
    margin: 0;
    padding: 0;
    width: 846px;
    height: 1200px;
    overflow: hidden;
    background: var(--black);
  }
  .flyer {
    position: relative;
    width: 846px;
    height: 1200px;
    background: var(--black);
    overflow: hidden;
    font-family: "PT Sans", sans-serif;
    color: var(--white);
  }
  .hero-photo {
    position: absolute;
    left: 0;
    top: 0;
    width: 846px;
    height: 600px;
    background:
      linear-gradient(180deg,
        var(--sky-top) 0%,
        var(--sky-mid) 25%,
        #c99a4a 45%,
        var(--horizon) 58%,
        #8a5c14 62%,
        var(--water) 75%,
        #120c04 88%,
        var(--black) 100%);
  }
  .corner-ribbon {
    position: absolute;
    top: 0;
    right: 0;
    width: 846px;
    height: 300px;
  }
  .corner-ribbon text {
    font-family: "Oswald", sans-serif;
    font-weight: 700;
    font-size: 32px;
    letter-spacing: 1px;
    fill: var(--black);
  }
  .program-title {
    position: absolute;
    top: 712px;
    left: 0;
    width: 846px;
    margin: 0;
    text-align: center;
    font-family: "Abril Fatface", serif;
    font-weight: 400;
    font-size: 104px;
    line-height: 1;
    letter-spacing: 10px;
    background: linear-gradient(180deg, var(--gold-light) 0%, var(--gold) 55%, var(--gold-deep) 100%);
    -webkit-background-clip: text;
    background-clip: text;
    color: transparent;
  }
  .program-summary {
    position: absolute;
    top: 828px;
    left: 40px;
    width: 766px;
    margin: 0;
    text-align: center;
    font-size: 22.5px;
    line-height: 29px;
  }
  .brand {
    position: absolute;
    top: 990px;
    left: 0;
    width: 846px;
    text-align: center;
  }
  .brand-mark {
    display: block;
    width: 44px;
    height: 44px;
    margin: 0 auto 26px;
    background: var(--gold);
  }
  .brand-name {
    font-family: "Raleway", sans-serif;
    font-weight: 300;
    font-size: 38px;
    letter-spacing: 2px;
    color: var(--gold);
    line-height: 1;
  }
  .contact {
    position: absolute;
    top: 1132px;
    left: 0;
    width: 846px;
    text-align: center;
    font-size: 21px;
    color: var(--white);
  }
  .contact-item { margin: 0 14px; }
  .contact-label {
    color: var(--gold);
    font-weight: 700;
    font-size: 15px;
    margin-right: 8px;
  }
</style>
</head>
<body>
  <main class="flyer">
    <div class="hero-photo" role="img" aria-label="Silhouette of a woman reaching towards the setting sun over calm water"></div>

    <svg class="corner-ribbon" viewBox="0 0 846 300" aria-hidden="false">
      <defs>
        <linearGradient id="ribbonGold" x1="0" y1="0" x2="1" y2="1">
          <stop offset="0" stop-color="#f3dc8a"/>
          <stop offset="1" stop-color="#c9a23e"/>
        </linearGradient>
      </defs>
      <polygon points="545,0 846,0 846,300" fill="url(#ribbonGold)"/>
      <text x="740" y="84" text-anchor="middle" transform="rotate(45 740 84)">TRAINING</text>
      <text x="722" y="132" text-anchor="middle" transform="rotate(45 722 132)">MENTORING</text>
    </svg>

    <h1 class="program-title">SKYWARD</h1>

    <p class="program-summary">This is one of our highest in-demand programs and is based on a back-ground and proven track record by Delia in accelerating sales organi-sations and their people into stand out high performers.</p>

    <div class="brand">
      <span class="brand-mark"></span>
      <div class="brand-name">DELIA MARSK</div>
    </div>

    <div class="contact">
      <span class="contact-item"><span class="contact-label">W</span>www.deliamarsk.example</span>
      <span class="contact-item"><span class="contact-label">E</span>delia@deliamarsk.example</span>
    </div>
  </main>
</body>
</html>
```